Cleaning Company needs a new business card design

Hi, We are looking for new business card designs to update with our latest logo and company information.
We would like to see designs using the colours:
Royal Blue #4169E1 - this is our company colour so this has to be in there. Please feel free to experiment with other colours.
Must include:
Front of business card:
Logo
Back of the business card:
0800 529 6081
07438 915 702
Email: info@pkrtidyhomes.co.uk
Web: www.pkrtidyhomes.co.uk
Services:
End of Tenancy
Carpet & Upholstery
Regular & One Off
all work fully insured.
The front of the business card with the logo can be made to look raised print. The blue man to be a shiny finish.
The business card needs to be presented in a matt finish
The business must be in the following styles:
Standard Square with rounded corners.
Thank you to all that take part in this.
Target Market(s)
Men and Women of different ages in the UK.
Industry/Entity Type
House Cleaning
Contact Information for Business Card
Front of business card:
Logo
0800 529 6081
07438 915 702
Email: pkrtidy@mailbox-demo.co.uk
Services:
End of Tenancy
Carpet & Upholstery
Regular & One Off
all work fully insured.

```html
<!DOCTYPE html>
<html lang="en">
<head>
<meta charset="utf-8">
<title>Business Card Design – Front Options</title>
<link rel="stylesheet" href="https://fonts.googleapis.com/css2?family=Oswald:wght@300;400;500;600&family=Nunito+Sans:wght@400;700&display=swap">
<style>
  :root {
    --sheet-light: #b9b9b9;
    --sheet-dark: #5a5a5a;
    --card-blue: #2f4a9e;
    --royal-blue: #4169e1;
    --callout-blue: #1b75bb;
    --accent-red: #e8202a;
    --ink: #1a1a1a;
    --panel-white: #ffffff;
    --panel-grey: #dcdcdc;
    --rule: #ffffff;
    --label: #b9c4e4;
    --sky-top: #b9d3ea;
    --sky-mid: #e7eef5;
    --sky-deep: #7fa6cf;
  }
  * { box-sizing: border-box; margin: 0; padding: 0; }
  html, body { width: 1200px; height: 1200px; overflow: hidden; }
  body {
    position: relative;
    font-family: "Oswald", sans-serif;
    background: radial-gradient(ellipse 70% 60% at 25% 50%, var(--sheet-light), var(--sheet-dark));
  }

  .sheet-title {
    position: absolute; left: 42px; top: 30px;
    color: #fff; font-weight: 600; font-size: 72px; line-height: 76px;
    letter-spacing: -0.5px;
  }
  .sheet-title .title-sub { display: block; margin-top: 26px; }

  .card {
    position: absolute; left: 308px; width: 584px; height: 384px;
    border-radius: 20px; overflow: hidden;
    background: var(--panel-white);
    box-shadow: 4px 6px 10px rgba(0,0,0,0.35);
  }
  .card--one { top: 11px; }
  .card--two { top: 408px; }
  .card--three { top: 805px; }

  .services-panel {
    position: absolute; left: 0; top: 0; width: 282px; height: 229px;
    background: linear-gradient(100deg, var(--panel-white) 15%, var(--panel-grey));
  }
  .services-list { position: absolute; left: 38px; top: 40px; list-style: none; }
  .services-list li {
    font-size: 26px; font-weight: 400; color: var(--ink); line-height: 30.5px;
    position: relative; padding-left: 18px;
  }
  .services-list li::before {
    content: ""; position: absolute; left: 0; top: 13px;
    width: 7px; height: 7px; border-radius: 50%; background: var(--accent-red);
  }
  .services-rule {
    position: absolute; left: 80px; top: 154px; width: 123px; height: 1px; background: #333;
  }
  .insured-line {
    position: absolute; left: 37px; top: 176px;
    font-size: 21px; font-weight: 600; color: var(--accent-red); letter-spacing: 0.2px;
  }

  .photo-area {
    position: absolute; left: 282px; top: 0; width: 302px; height: 138px;
    background: linear-gradient(160deg, var(--sky-top), var(--sky-mid) 45%, var(--sky-deep));
  }
  .card--three .photo-area { height: 229px; }

  .badge-area, .tagline-area {
    position: absolute; left: 282px; top: 138px; width: 302px; height: 91px; background: var(--panel-white);
  }
  .pointer { position: absolute; width: 28px; height: 14px; }
  .badge-area .pointer, .tagline-area .pointer { left: 212px; top: 0; }
  .badge-lead { position: absolute; left: 0; width: 100%; top: 12px; text-align: center;
    font-family: "Nunito Sans", sans-serif; font-size: 14px; color: var(--ink); }
  .badge-name { position: absolute; left: 0; width: 100%; top: 28px; text-align: center;
    font-family: "Oswald", sans-serif; font-weight: 500; font-size: 30px; line-height: 36px; color: var(--accent-red); }
  .badge-since { position: absolute; right: 30px; top: 66px;
    font-family: "Nunito Sans", sans-serif; font-size: 14px; color: var(--ink); }

  .tagline { position: absolute; left: 0; width: 100%; top: 34px; text-align: center;
    font-size: 26px; font-weight: 400; color: var(--ink); }
  .tagline .dot { color: var(--accent-red); margin: 0 8px; font-size: 20px; vertical-align: 3px; }

  .contact-band {
    position: absolute; left: 0; top: 229px; width: 584px; height: 155px; background: var(--card-blue);
    color: #fff;
  }
  .card--three .contact-band .pointer { left: 508px; top: 0; }
  .field-label {
    position: absolute; display: flex; align-items: center; gap: 6px;
    font-size: 12px; font-weight: 300; color: var(--label); letter-spacing: 0.3px;
  }
  .field-label svg { width: 13px; height: 11px; }
  .field-label .rule { height: 1px; background: var(--rule); position: relative; margin-left: 4px; }
  .field-label .rule::after { content: ""; position: absolute; right: -2px; top: -2px;
    width: 5px; height: 5px; border-radius: 50%; background: var(--rule); }
  .label-call { left: 38px; top: 13px; }
  .label-call .rule { width: 118px; }
  .label-mail { left: 247px; top: 13px; }
  .label-mail .rule { width: 230px; }
  .card--three .label-mail .rule { width: 166px; }
  .label-web { left: 247px; top: 76px; }
  .label-web .rule { width: 250px; }

  .phone { position: absolute; left: 37px; font-size: 33px; font-weight: 400; line-height: 44px; letter-spacing: -0.6px; white-space: nowrap; }
  .phone--main { top: 36px; }
  .phone--mobile { top: 87px; }
  .contact-text { position: absolute; left: 247px; font-size: 31px; font-weight: 300; line-height: 36px; letter-spacing: -0.3px; white-space: nowrap; }
  .contact-email { top: 34px; }
  .contact-web { top: 94px; }

  .option-callout { position: absolute; left: 918px; width: 219px; height: 114px; }
  .option-callout svg { position: absolute; inset: 0; filter: drop-shadow(3px 4px 4px rgba(0,0,0,0.35)); }
  .option-callout p { position: absolute; left: 19px; width: 190px; top: 0; height: 114px;
    display: flex; align-items: center; justify-content: center; text-align: center;
    color: #fff; font-weight: 500; font-size: 21px; line-height: 26px; }
  .callout-one { top: 147px; }
  .callout-two { top: 544px; }
  .callout-three { top: 939px; }
</style>
</head>
<body>

<svg width="0" height="0" style="position:absolute">
  <defs>
    <symbol id="icon-phone" viewBox="0 0 16 16"><path d="M3 1l3 3-1.5 2a9 9 0 0 0 5.5 5.5L12 10l3 3-2 2C7 15 1 9 1 3z" fill="currentColor"/></symbol>
    <symbol id="icon-mail" viewBox="0 0 16 12"><rect x="0.5" y="0.5" width="15" height="11" fill="currentColor"/><path d="M1 1l7 6 7-6" stroke="#2f4a9e" fill="none" stroke-width="1.2"/></symbol>
    <symbol id="icon-globe" viewBox="0 0 16 16"><circle cx="8" cy="8" r="7" fill="currentColor"/><path d="M1 8h14M8 1c-3 4-3 10 0 14M8 1c3 4 3 10 0 14" stroke="#2f4a9e" fill="none" stroke-width="1"/></symbol>
    <symbol id="callout-shape" viewBox="0 0 219 114"><path d="M19 0h190v114H19V75L0 57l19-18z" fill="#1b75bb"/></symbol>
  </defs>
</svg>

<h1 class="sheet-title">Biz Card<br>Design<span class="title-sub">(Front)</span></h1>

<!-- Option 1 -->
<section class="card card--one">
  <div class="services-panel">
    <ul class="services-list"><li>End of Tenancy</li><li>Carpet &amp; Upholstery</li><li>Regular &amp; One Off</li></ul>
    <div class="services-rule"></div>
    <p class="insured-line">ALL WORK FULLY INSURED</p>
  </div>
  <div class="photo-area" role="img" aria-label="Photo of a woman cleaning a window with a yellow cloth against a blue sky"></div>
  <div class="badge-area">
    <svg class="pointer" viewBox="0 0 28 14"><path d="M0 0h28L14 14z" fill="#c6d7e8"/></svg>
    <p class="badge-lead">Highly Recommended on</p>
    <p class="badge-name">TrustedTrades.net</p>
    <p class="badge-since">Member since Dec 2013</p>
  </div>
  <div class="contact-band">
    <div class="field-label label-call"><svg><use href="#icon-phone"/></svg>CALL US<span class="rule"></span></div>
    <p class="phone phone--main">0800 529 6081</p>
    <p class="phone phone--mobile">07438 915 702</p>
    <div class="field-label label-mail"><svg><use href="#icon-mail"/></svg>E-MAIL<span class="rule"></span></div>
    <p class="contact-text contact-email">info@pkrtidyhomes.co.uk</p>
    <div class="field-label label-web"><svg><use href="#icon-globe"/></svg>WEB<span class="rule"></span></div>
    <p class="contact-text contact-web">www.pkrtidyhomes.co.uk</p>
  </div>
</section>

<!-- Option 2 -->
<section class="card card--two">
  <div class="services-panel">
    <ul class="services-list"><li>End of Tenancy</li><li>Carpet &amp; Upholstery</li><li>Regular &amp; One Off</li></ul>
    <div class="services-rule"></div>
    <p class="insured-line">ALL WORK FULLY INSURED</p>
  </div>
  <div class="photo-area" role="img" aria-label="Photo of a woman cleaning a window with a yellow cloth against a blue sky"></div>
  <div class="tagline-area">
    <svg class="pointer" viewBox="0 0 28 14"><path d="M0 0h28L14 14z" fill="#c6d7e8"/></svg>
    <p class="tagline">Quality<span class="dot">•</span>Efficiency<span class="dot">•</span>Value</p>
  </div>
  <div class="contact-band">
    <div class="field-label label-call"><svg><use href="#icon-phone"/></svg>CALL US<span class="rule"></span></div>
    <p class="phone phone--main">0800 529 6081</p>
    <p class="phone phone--mobile">07438 915 702</p>
    <div class="field-label label-mail"><svg><use href="#icon-mail"/></svg>E-MAIL<span class="rule"></span></div>
    <p class="contact-text contact-email">info@pkrtidyhomes.co.uk</p>
    <div class="field-label label-web"><svg><use href="#icon-globe"/></svg>WEB<span class="rule"></span></div>
    <p class="contact-text contact-web">www.pkrtidyhomes.co.uk</p>
  </div>
</section>

<!-- Option 3 -->
<section class="card card--three">
  <div class="services-panel">
    <ul class="services-list"><li>End of Tenancy</li><li>Carpet &amp; Upholstery</li><li>Regular &amp; One Off</li></ul>
    <div class="services-rule"></div>
    <p class="insured-line">ALL WORK FULLY INSURED</p>
  </div>
  <div class="photo-area" role="img" aria-label="Full-height photo of a woman cleaning a window with a yellow cloth against a blue sky"></div>
  <div class="contact-band">
    <svg class="pointer" viewBox="0 0 28 14"><path d="M0 0h28L14 14z" fill="#9fbcd9"/></svg>
    <div class="field-label label-call"><svg><use href="#icon-phone"/></svg>CALL US<span class="rule"></span></div>
    <p class="phone phone--main">0800 529 6081</p>
    <p class="phone phone--mobile">07438 915 702</p>
    <div class="field-label label-mail"><svg><use href="#icon-mail"/></svg>E-MAIL<span class="rule"></span></div>
    <p class="contact-text contact-email">info@pkrtidyhomes.co.uk</p>
    <div class="field-label label-web"><svg><use href="#icon-globe"/></svg>WEB<span class="rule"></span></div>
    <p class="contact-text contact-web">www.pkrtidyhomes.co.uk</p>
  </div>
</section>

<div class="option-callout callout-one"><svg viewBox="0 0 219 114"><use href="#callout-shape"/></svg><p>Option 1<br>Front with<br>TrustedTrades Logo</p></div>
<div class="option-callout callout-two"><svg viewBox="0 0 219 114"><use href="#callout-shape"/></svg><p>Option 2<br>Front with<br>Slogan / Tagline</p></div>
<div class="option-callout callout-three"><svg viewBox="0 0 219 114"><use href="#callout-shape"/></svg><p>Option 3<br>Front with<br>Full Photo</p></div>

</body>
</html>
```